Beacon Advisory Website

I currently have a website www.beaconadvisoryinc.example. We are a IT Consulting Company. Our website will pretty much tell out our services. I am looking to enhance my website and make it look more professional. Looking for very classy and Contemporary look and design for my website.

Industry/Entity Type

It Company

```html
<!DOCTYPE html>
<html lang="en">
<head>
<meta charset="utf-8">
<title>Beacon Advisory</title>
<link href="https://fonts.googleapis.com/css2?family=Open+Sans:wght@400;600;700&display=swap" rel="stylesheet">
<style>
:root{
  --brand:#1a5ea8;
  --sky:#0a9ee0;
  --sky-light:#8fd0f2;
  --ink:#1d1d1d;
  --text:#555;
  --band:#ebebeb;
  --white:#fff;
  --footer:#1b79b8;
  --bar:#111;
}
*{margin:0;padding:0;box-sizing:border-box}
html,body{width:1200px;height:3543px;overflow:hidden}
body{position:relative;font-family:"Open Sans",Arial,sans-serif;color:var(--text);background:var(--white)}
.abs{position:absolute}
.center{left:0;width:1200px;text-align:center}

/* header / hero */
.hero{top:0;left:0;width:1200px;height:784px;overflow:hidden}
.hero-photo{position:absolute;inset:0;background:
  linear-gradient(90deg,#eceff1 0%,#8e959c 5%,#6c737a 12%,#d9dde1 20%,#e4d2c4 30%,#c9d8ea 40%,#b7cbe2 50%,#e8ddd3 62%,#d8c3b2 72%,#f3f4f5 82%,#e9ecee 100%)}
.hero-wave{position:absolute;left:0;top:560px}
.logo{top:34px;left:106px;display:flex;align-items:center;gap:12px;white-space:nowrap}
.logo-mark{width:40px;height:40px;background:var(--brand)}
.logo-name{font-size:28px;font-weight:700;color:var(--brand);line-height:1}
.nav{top:38px;left:465px;display:flex;font-size:17px;color:var(--ink);white-space:nowrap}
.nav a{display:block;height:40px;line-height:40px;padding:0 7px;color:var(--ink);text-decoration:none}
.nav a.active{background:var(--brand);color:var(--white);margin-right:8px;padding:0 14px}

/* sections */
.section-title{font-size:40px;font-weight:400;color:var(--brand);letter-spacing:1px}
.welcome-icon{top:850px;left:576px;width:48px;height:48px;background:var(--brand);border-radius:50%}
.welcome-title{top:896px;font-size:46px;font-weight:400;color:var(--ink);letter-spacing:1px}
.welcome-title span{color:var(--brand)}
.welcome-text{top:990px;left:140px;width:930px;text-align:center;font-size:16px;line-height:26px}

.service{top:1238px;width:280px;text-align:center}
.service-icon{width:85px;height:85px;margin:0 auto;border-radius:50%;background:var(--sky);display:flex;align-items:center;justify-content:center}
.service h3{margin-top:22px;font-size:20px;font-weight:400;color:var(--ink);letter-spacing:.5px;white-space:nowrap}
.service p{margin:18px auto 0;width:240px;font-size:15px;line-height:25px}

.solutions-band{top:1507px;left:0;width:1200px;height:583px;background:var(--band)}
.card{top:1625px;width:312px;height:397px;background:var(--white)}
.card-photo{height:220px}
.card h3{margin:24px 0 0 24px;font-size:21px;font-weight:400;color:var(--ink)}
.card p{margin:14px 24px 0 24px;font-size:15px;line-height:24px}

.resource-photo{top:2220px;width:260px;height:248px}
.resource{top:2262px;width:230px}
.resource h3{font-size:19px;font-weight:400;color:var(--ink)}
.resource p{margin-top:20px;font-size:15px;line-height:25px}

.contact-band{top:2520px;left:0;width:1200px;height:499px;background:var(--band)}
.field{left:168px;width:368px;height:48px;background:var(--white);font-size:15px;color:#999;padding:12px 14px}
.message{top:2652px;left:574px;width:451px;height:213px;background:var(--white);font-size:15px;color:#999;padding:12px 20px}
.send{top:2929px;left:529px;width:139px;height:35px;background:var(--brand);color:var(--white);font-size:18px;text-align:center;line-height:35px}

.footer{top:3019px;left:0;width:1200px;height:472px;background:linear-gradient(135deg,#0c5f9c 0%,#2a8fcf 45%,#136aa9 100%)}
.panel{top:3082px;left:295px;width:607px;height:373px;background:rgba(255,255,255,.2)}
.keep{top:3108px;font-size:28px;font-weight:400;color:var(--white);letter-spacing:1px}
.c-icon{width:40px;height:40px;border-radius:50%;background:var(--white);display:flex;align-items:center;justify-content:center}
.c-text{font-size:16px;color:var(--white);white-space:nowrap}
.bottom-bar{top:3491px;left:0;width:1200px;height:52px;background:var(--bar);color:var(--white);font-size:15px;line-height:52px;text-align:center}
</style>
</head>
<body>

<header class="abs hero">
  <div class="hero-photo" role="img" aria-label="Photo of two smiling colleagues looking at a tablet beside a desktop computer in a bright office"></div>
  <svg class="hero-wave" width="1200" height="224" viewBox="0 0 1200 224">
    <path d="M0 30 C300 150 800 170 1200 40 L1200 224 L0 224 Z" fill="var(--sky-light)"/>
    <path d="M0 60 C320 175 820 185 1200 70 L1200 224 L0 224 Z" fill="var(--white)"/>
    <path d="M0 80 C320 195 820 205 1200 90 L1200 224 L0 224 Z" fill="var(--sky)"/>
  </svg>
  <div class="abs logo"><span class="logo-mark"></span><span class="logo-name">BEACON ADVISORY</span></div>
  <nav class="abs nav">
    <a class="active">COMPANY</a><a>SERVICES</a><a>SOLUTION</a><a>RESOURCES</a><a>CAREER</a><a>CONTACT US</a>
  </nav>
</header>

<section class="welcome">
  <div class="abs welcome-icon"></div>
  <h1 class="abs center welcome-title">WELCOME TO <span>BEACON ADVISORY</span></h1>
  <p class="abs welcome-text">Delivers highest level of Quality Consultants and services for the lowest Cost of Ownership. Forge Client relationships to better understand and respond to their business needs.Forge Client relationships to better understand and respond to their business needs.Develop, challenge, empower and recognize our employees .</p>
</section>

<section class="services">
  <h2 class="abs center section-title" style="top:1145px">SERVICES</h2>
  <div class="abs service" style="left:63px">
    <div class="service-icon"><svg width="40" height="40" viewBox="0 0 40 40"><rect x="12" y="5" width="16" height="30" rx="3" fill="none" stroke="#fff" stroke-width="2.5"/><circle cx="20" cy="30" r="1.8" fill="#fff"/></svg></div>
    <h3>TECHNOLOGY</h3>
    <p>Beacon Advisory Training programs are perfect&nbsp; to enhance their careers.</p>
  </div>
  <div class="abs service" style="left:318px">
    <div class="service-icon"><svg width="44" height="44" viewBox="0 0 44 44"><circle cx="22" cy="13" r="6" fill="#fff"/><path d="M10 38 C10 26 34 26 34 38 Z" fill="#fff"/></svg></div>
    <h3>OFFSHORE</h3>
    <p>Our Offshore development model has a unique distinction software solutions</p>
  </div>
  <div class="abs service" style="left:573px">
    <div class="service-icon"><svg width="44" height="44" viewBox="0 0 44 44"><circle cx="17" cy="24" r="8" fill="none" stroke="#fff" stroke-width="5" stroke-dasharray="4 2.3"/><circle cx="30" cy="13" r="5" fill="none" stroke="#fff" stroke-width="3.5" stroke-dasharray="3 1.8"/></svg></div>
    <h3>APPLICATON DEVLOPMENT</h3>
    <p>Drawing on our experience in all major industries,</p>
  </div>
  <div class="abs service" style="left:859px">
    <div class="service-icon"><svg width="44" height="44" viewBox="0 0 44 44"><circle cx="22" cy="22" r="11" fill="none" stroke="#fff" stroke-width="7" stroke-dasharray="5 3.6"/><circle cx="22" cy="22" r="4" fill="#fff"/></svg></div>
    <h3>ENTERPRISE INTEGRATION</h3>
    <p>As organizations work to achieve and sustain competitive advantage.</p>
  </div>
</section>

<section class="solutions">
  <div class="abs solutions-band"></div>
  <h2 class="abs center section-title" style="top:1555px">SOLUTIONS</h2>
  <article class="abs card" style="left:99px">
    <div class="card-photo" role="img" aria-label="Photo of people working with laptops and notebooks at a desk, seen from above" style="background:linear-gradient(135deg,#c9b79c,#eae4d8 60%,#6f7c8a)"></div>
    <h3>Dashboard</h3>
    <p>Dashboards are a key component of every organization's Performance Management .</p>
  </article>
  <article class="abs card" style="left:449px">
    <div class="card-photo" role="img" aria-label="Photo of a businessman touching floating virtual screens" style="background:linear-gradient(90deg,#2b2b2b,#8c8f93 55%,#c7d3df)"></div>
    <h3>Data warehousing</h3>
    <p>A data warehouse is the concept of data extracted from operational systems and made available as historical snapshots</p>
  </article>
  <article class="abs card" style="left:789px">
    <div class="card-photo" role="img" aria-label="Photo of two businessmen discussing documents" style="background:linear-gradient(135deg,#e8e6e2,#9a9590 50%,#3a3f4a)"></div>
    <h3>BPM</h3>
    <p>Beacon Advisory having Flowline Certified Consultants in to provide Business Process Management .</p>
  </article>
</section>

<section class="resources">
  <h2 class="abs center section-title" style="top:2135px">RESOURCES</h2>
  <div class="abs resource-photo" style="left:78px;background:linear-gradient(135deg,#0a1a3a,#1f5fa8 55%,#0b2450)" role="img" aria-label="Photo of a hand touching glowing digital interface squares"></div>
  <div class="abs resource" style="left:361px">
    <h3>Our Process</h3>
    <p>We bring together seasoned IT executives and battle-tested computer support personnel, provide them with the right resources for the job,</p>
  </div>
  <div class="abs resource-photo" style="left:602px;background:linear-gradient(135deg,#d4d6d8,#f1f2f3 50%,#a9adb2)" role="img" aria-label="Photo of a team meeting around a white table, seen from above"></div>
  <div class="abs resource" style="left:886px">
    <h3>Staff Augmentation</h3>
    <p>For years Beacon Advisory has been offering our customers the ability to augment their existing staff with temporary highly skilled IT professionals .</p>
  </div>
</section>

<section class="contact">
  <div class="abs contact-band"></div>
  <h2 class="abs center section-title" style="top:2565px">CONTACT US</h2>
  <div class="abs field" style="top:2652px">Name</div>
  <div class="abs field" style="top:2733px">Email</div>
  <div class="abs field" style="top:2825px">Phone</div>
  <div class="abs message">Message</div>
  <div class="abs send">Send Mail</div>
</section>

<footer>
  <div class="abs footer" role="img" aria-label="Photo of glass office towers seen from below, tinted blue"></div>
  <div class="abs panel"></div>
  <h2 class="abs center keep">KEEP IN TOUCH</h2>
  <div class="abs c-icon" style="top:3195px;left:377px"><svg width="20" height="20" viewBox="0 0 20 20"><path d="M5 2 L8 6 L6.5 8 C7.5 10.5 9.5 12.5 12 13.5 L14 12 L18 15 L16 18 C9 18 2 11 2 4 Z" fill="var(--footer)"/></svg></div>
  <div class="abs c-text" style="top:3204px;left:428px">+1 (555) 014-2290</div>
  <div class="abs c-icon" style="top:3195px;left:585px"><svg width="20" height="20" viewBox="0 0 20 20"><rect x="2" y="4" width="16" height="12" fill="none" stroke="var(--footer)" stroke-width="2"/><path d="M2 4 L10 11 L18 4" fill="none" stroke="var(--footer)" stroke-width="2"/></svg></div>
  <div class="abs c-text" style="top:3204px;left:640px">info@beaconadvisory.example</div>
  <div class="abs c-icon" style="top:3277px;left:377px"><svg width="20" height="20" viewBox="0 0 20 20"><path d="M10 1 C5.5 1 3 4 3 7.5 C3 12 10 19 10 19 C10 19 17 12 17 7.5 C17 4 14.5 1 10 1 Z" fill="var(--footer)"/><circle cx="10" cy="7.5" r="2.5" fill="#fff"/></svg></div>
  <div class="abs c-text" style="top:3286px;left:428px">48 Meridian Ave,Suite 310,Fairview, NJ 07999</div>
  <div class="abs c-icon" style="top:3334px;left:495px"></div>
  <div class="abs c-icon" style="top:3334px;left:568px"></div>
  <div class="abs c-icon" style="top:3334px;left:630px"></div>
  <div class="abs bottom-bar">© <strong>BEACON ADVISORY</strong> -2016.All Rights Reserved.</div>
</footer>

</body>
</html>
```